Luxury Wine Label for New Startup Winery

We need a wine label for our new winery startup. We have worked with a local designer but do not feel the resulting label / logo have the elevation required to present our brand as a luxury wine. Our winery is called "Harrowgate Vineyards" and we are focused on extremely high quality hand crafted artisan and estate wines from the Pacific Northwest.
We would like to see designs that utilize a tree line, or other imagery that represents the "Harrowgate" part of our company name. Another interesting feature could be wood grain.
A logo will be required based on your design so please design with this in mind:
This logo should be consistent with the wine bottle label design, and should be representative of our high end exclusive wine while giving a sense of place (Oregon/ Pacific Northwest.)
I will supply an image of the design we received from our local designer, PLEASE NOTE: in general we do like wood grain and tree line concepts but feel the execution was poorly done.
ATTN: Logo design should be suitable for use on: Bottles (Red wine/rose/white wine), Bussiness cards, vehicle signage, business signage, etc
P.S.:
If you have a design that is not outside the box we are still interested in seeing it.
Label is for a burgundy style bottle with a label height of 3.5 - 4" and a width of 3.5-4"
any label <= 4"x4" and >=3.5"x3.5" will be acceptable:
HOWEVER Width should be greater than or equal to height due to the bottle format
Target Market(s)
Wine enthusiasts with adequate discretionary budgets to afford $100 bottles of wine.
Industry/Entity Type
Wine / Winery
Requirements
Must have
- A sense of luxury, a feel of exclusivity, and a theme consistent with our product and brand name
Nice to have
- Tree line, wood grain or other wood themes. Serif fonts
Should not have
- anything cheesy, off topic, hard to read script fonts or anything that makes the label hard to read from a few feet away or too busy

```html
<!DOCTYPE html>
<html lang="en">
<head>
<meta charset="utf-8">
<title>Harrowgate Vineyards – Label Range</title>
<link rel="stylesheet" href="https://fonts.googleapis.com/css2?family=Cinzel:wght@500;600&family=Libre+Baskerville&display=swap">
<style>
  :root {
    --page: #f1f1f0;
    --gold-light: #f6dc93;
    --gold: #c9963f;
    --gold-deep: #7d4f18;

    --merlot-ground: #141213;
    --merlot-band: #3a2b2d;
    --merlot-grain: #231b1c;
    --merlot-soil: #3e3033;
    --merlot-brand: #d9a956;
    --merlot-text: #e4dcd6;

    --chard-ground: #6e5a2c;
    --chard-band: #1e1c1a;
    --chard-grain: #2a251d;
    --chard-soil: #8a7440;
    --chard-brand: #e0b15e;
    --chard-text: #d9c79c;

    --rose-ground: #efe2c4;
    --rose-band: #f1efeb;
    --rose-grain: #ecdfc2;
    --rose-soil: #f6f1e6;
    --rose-brand: #d6b272;
    --rose-text: #2a2321;
  }

  * { box-sizing: border-box; margin: 0; padding: 0; }

  html, body {
    width: 1200px;
    height: 1200px;
    overflow: hidden;
    background: var(--page);
  }

  .range {
    width: 1200px;
    height: 1200px;
    display: flex;
    justify-content: center;
    align-items: center;
    gap: 40px;
  }

  .label {
    position: relative;
    width: 340px;
    height: 380px;
    filter: drop-shadow(0 10px 18px rgba(0,0,0,0.12));
  }

  .label--merlot {
    --ground: var(--merlot-ground); --band: var(--merlot-band);
    --grain: var(--merlot-grain); --soil: var(--merlot-soil);
    --brand: var(--merlot-brand); --varietal: var(--merlot-text);
  }
  .label--chardonnay {
    --ground: var(--chard-ground); --band: var(--chard-band);
    --grain: var(--chard-grain); --soil: var(--chard-soil);
    --brand: var(--chard-brand); --varietal: var(--chard-text);
  }
  .label--rose {
    --ground: var(--rose-ground); --band: var(--rose-band);
    --grain: var(--rose-grain); --soil: var(--rose-soil);
    --brand: var(--rose-brand); --varietal: var(--rose-text);
  }

  .label__art { position: absolute; inset: 0; width: 340px; height: 380px; }
  .art-ground { fill: var(--ground); }
  .art-band { fill: var(--band); }
  .art-soil { fill: var(--soil); }
  .art-edge { fill: none; stroke: var(--gold); stroke-width: 2.5; }
  .art-edge--heavy { stroke-width: 5; }

  .label__brand {
    position: absolute;
    top: 26px;
    left: 0;
    width: 100%;
    text-align: center;
    font-family: "Cinzel", serif;
    color: var(--brand);
  }
  .label__name {
    display: block;
    font-size: 31px;
    font-weight: 600;
    letter-spacing: 0.07em;
    line-height: 1;
  }
  .label__sub {
    display: block;
    margin-top: 6px;
    font-size: 18px;
    font-weight: 600;
    letter-spacing: 0.24em;
    line-height: 1;
  }

  .label__varietal {
    position: absolute;
    top: 184px;
    left: 0;
    width: 100%;
    height: 36px;
    line-height: 36px;
    text-align: center;
    font-family: "Libre Baskerville", serif;
    font-size: 18px;
    letter-spacing: 0.06em;
    color: var(--varietal);
  }
</style>
</head>
<body>
  <main class="range">

    <article class="label label--merlot">
      <svg class="label__art" viewBox="0 0 340 380" aria-hidden="true">
        <defs>
          <linearGradient id="foil-merlot" x1="0" y1="0" x2="1" y2="0">
            <stop offset="0" style="stop-color:var(--gold-deep)"/>
            <stop offset="0.3" style="stop-color:var(--gold-light)"/>
            <stop offset="0.55" style="stop-color:var(--gold)"/>
            <stop offset="0.8" style="stop-color:var(--gold-light)"/>
            <stop offset="1" style="stop-color:var(--gold-deep)"/>
          </linearGradient>
          <linearGradient id="grain-merlot" x1="0" y1="0" x2="0" y2="1">
            <stop offset="0" style="stop-color:var(--grain)"/>
            <stop offset="0.5" style="stop-color:var(--gold-deep)"/>
            <stop offset="1" style="stop-color:var(--grain)"/>
          </linearGradient>
        </defs>
        <path class="art-ground" d="M0,14 C30,4 50,10 70,6 C100,0 120,12 150,8 C185,2 210,10 240,5 C280,0 310,12 340,6 L340,350 C310,340 290,372 260,360 C230,350 200,376 170,366 C140,356 110,378 80,364 C50,352 25,374 0,360 Z"/>
        <rect class="art-band" x="0" y="176" width="340" height="56"/>
        <g role="img" aria-label="Gold foil tree line silhouette over mountain ridge">
          <path fill="url(#foil-merlot)" d="M0,150 C30,128 60,120 90,118 C120,116 140,100 170,108 C200,116 230,98 260,104 C290,110 315,120 340,140 L340,178 C300,184 260,172 220,180 C180,188 120,174 80,182 C50,188 20,180 0,184 Z"/>
        </g>
        <g role="img" aria-label="Gold foil wood grain pattern">
          <path fill="url(#grain-merlot)" d="M0,238 C40,230 80,242 120,234 C170,226 220,240 260,232 C300,226 320,236 340,232 L340,300 L0,300 Z"/>
          <path class="art-edge" d="M0,238 C40,230 80,242 120,234 C170,226 220,240 260,232 C300,226 320,236 340,232"/>
        </g>
        <g role="img" aria-label="Textured earth layers with torn gold edge">
          <path class="art-soil" d="M0,300 C60,294 120,306 180,298 C240,292 290,304 340,298 L340,340 C300,334 250,348 200,340 C150,334 80,348 0,340 Z"/>
          <path class="art-edge" d="M0,300 C60,294 120,306 180,298 C240,292 290,304 340,298"/>
          <path class="art-edge art-edge--heavy" d="M0,360 C25,374 50,352 80,364 C110,378 140,356 170,366 C200,376 230,350 260,360 C290,372 310,340 340,350"/>
        </g>
      </svg>
      <header class="label__brand">
        <span class="label__name">HARROWGATE</span>
        <span class="label__sub">VINEYARDS</span>
      </header>
      <div class="label__varietal">MERLOT</div>
    </article>

    <article class="label label--chardonnay">
      <svg class="label__art" viewBox="0 0 340 380" aria-hidden="true">
        <defs>
          <linearGradient id="foil-chardonnay" x1="0" y1="0" x2="1" y2="0">
            <stop offset="0" style="stop-color:var(--gold-deep)"/>
            <stop offset="0.3" style="stop-color:var(--gold-light)"/>
            <stop offset="0.55" style="stop-color:var(--gold)"/>
            <stop offset="0.8" style="stop-color:var(--gold-light)"/>
            <stop offset="1" style="stop-color:var(--gold-deep)"/>
          </linearGradient>
          <linearGradient id="grain-chardonnay" x1="0" y1="0" x2="0" y2="1">
            <stop offset="0" style="stop-color:var(--grain)"/>
            <stop offset="0.5" style="stop-color:var(--gold-deep)"/>
            <stop offset="1" style="stop-color:var(--grain)"/>
          </linearGradient>
        </defs>
        <path class="art-ground" d="M0,14 C30,4 50,10 70,6 C100,0 120,12 150,8 C185,2 210,10 240,5 C280,0 310,12 340,6 L340,350 C310,340 290,372 260,360 C230,350 200,376 170,366 C140,356 110,378 80,364 C50,352 25,374 0,360 Z"/>
        <rect class="art-band" x="0" y="176" width="340" height="56"/>
        <g role="img" aria-label="Gold foil tree line silhouette over mountain ridge">
          <path fill="url(#foil-chardonnay)" d="M0,150 C30,128 60,120 90,118 C120,116 140,100 170,108 C200,116 230,98 260,104 C290,110 315,120 340,140 L340,178 C300,184 260,172 220,180 C180,188 120,174 80,182 C50,188 20,180 0,184 Z"/>
        </g>
        <g role="img" aria-label="Gold foil wood grain pattern">
          <path fill="url(#grain-chardonnay)" d="M0,238 C40,230 80,242 120,234 C170,226 220,240 260,232 C300,226 320,236 340,232 L340,300 L0,300 Z"/>
          <path class="art-edge" d="M0,238 C40,230 80,242 120,234 C170,226 220,240 260,232 C300,226 320,236 340,232"/>
        </g>
        <g role="img" aria-label="Textured earth layers with torn gold edge">
          <path class="art-soil" d="M0,300 C60,294 120,306 180,298 C240,292 290,304 340,298 L340,340 C300,334 250,348 200,340 C150,334 80,348 0,340 Z"/>
          <path class="art-edge" d="M0,300 C60,294 120,306 180,298 C240,292 290,304 340,298"/>
          <path class="art-edge art-edge--heavy" d="M0,360 C25,374 50,352 80,364 C110,378 140,356 170,366 C200,376 230,350 260,360 C290,372 310,340 340,350"/>
        </g>
      </svg>
      <header class="label__brand">
        <span class="label__name">HARROWGATE</span>
        <span class="label__sub">VINEYARDS</span>
      </header>
      <div class="label__varietal">CHARDONNAY</div>
    </article>

    <article class="label label--rose">
      <svg class="label__art" viewBox="0 0 340 380" aria-hidden="true">
        <defs>
          <linearGradient id="foil-rose" x1="0" y1="0" x2="1" y2="0">
            <stop offset="0" style="stop-color:var(--gold-deep)"/>
            <stop offset="0.3" style="stop-color:var(--gold-light)"/>
            <stop offset="0.55" style="stop-color:var(--gold)"/>
            <stop offset="0.8" style="stop-color:var(--gold-light)"/>
            <stop offset="1" style="stop-color:var(--gold-deep)"/>
          </linearGradient>
          <linearGradient id="grain-rose" x1="0" y1="0" x2="0" y2="1">
            <stop offset="0" style="stop-color:var(--grain)"/>
            <stop offset="0.5" style="stop-color:var(--gold-light)"/>
            <stop offset="1" style="stop-color:var(--grain)"/>
          </linearGradient>
        </defs>
        <path class="art-ground" d="M0,14 C30,4 50,10 70,6 C100,0 120,12 150,8 C185,2 210,10 240,5 C280,0 310,12 340,6 L340,350 C310,340 290,372 260,360 C230,350 200,376 170,366 C140,356 110,378 80,364 C50,352 25,374 0,360 Z"/>
        <rect class="art-band" x="0" y="176" width="340" height="56"/>
        <g role="img" aria-label="Gold foil tree line silhouette over mountain ridge">
          <path fill="url(#foil-rose)" d="M0,150 C30,128 60,120 90,118 C120,116 140,100 170,108 C200,116 230,98 260,104 C290,110 315,120 340,140 L340,178 C300,184 260,172 220,180 C180,188 120,174 80,182 C50,188 20,180 0,184 Z"/>
        </g>
        <g role="img" aria-label="Gold foil wood grain pattern">
          <path fill="url(#grain-rose)" d="M0,238 C40,230 80,242 120,234 C170,226 220,240 260,232 C300,226 320,236 340,232 L340,300 L0,300 Z"/>
          <path class="art-edge" d="M0,238 C40,230 80,242 120,234 C170,226 220,240 260,232 C300,226 320,236 340,232"/>
        </g>
        <g role="img" aria-label="Textured earth layers with torn gold edge">
          <path class="art-soil" d="M0,300 C60,294 120,306 180,298 C240,292 290,304 340,298 L340,340 C300,334 250,348 200,340 C150,334 80,348 0,340 Z"/>
          <path class="art-edge" d="M0,300 C60,294 120,306 180,298 C240,292 290,304 340,298"/>
          <path class="art-edge art-edge--heavy" d="M0,360 C25,374 50,352 80,364 C110,378 140,356 170,366 C200,376 230,350 260,360 C290,372 310,340 340,350"/>
        </g>
      </svg>
      <header class="label__brand">
        <span class="label__name">HARROWGATE</span>
        <span class="label__sub">VINEYARDS</span>
      </header>
      <div class="label__varietal">ROSE</div>
    </article>

  </main>
</body>
</html>
```